Web Design (Coded) and Project - Finance Company

Corvale Lending Group is a mortgage broker company based in Sydney Australia and provides lending solutions for individuals and businesses.

Our target market is anyone with the financial means to get a loan.

I am looking for a website design in this contest. The site needs to be able to be viewed on a portable device such as Tabra, Fonix, etc.

I have the logo design and files which need to be used. I also have the NLBC logo which will need to be in the footer of each page.

The website needs to represent a big finance company with integrity and knowledge.

The website will need to be uploaded to Hostwillow.example.au as they are the hosting provider. I will also need the ability to make changes to the text and pictures in the future and upload the revisions. I need the website ready to go and ready to be uploaded onto Host Willow.

The website will consist of 6 pages in total There are 4 main pages that will be viewed and then 2 with Privacy and Internal Dispute Resolution which are only accessed through links. These will be as follows:

Home
I would prefer to have a fresh bright and professional looking home page given that most mortgage broker websites look the same with the menu buttons at the top.

Services
Details the loan types that we handle and some text for each one.

About Us
I have the text for this.

Contact Us
Form to have the following inputs:
• Surname
• First Name
• Suburb
• State
• Phone number
• Mobile number
• Email address
• Preferred contact
o Phone
o Mobile
o Email
• Reason for Enquiry
o First home buyer
o Refinance
o Investment Property
o Commercial lending
o Personal loan
o Other
• Comments

Privacy
This page will only be accessed from a link at the bottom of each page. I have the wording that I will provide.

Dispute Resolution Policy
This page will only be accessed from a link on the Contact Us page. I have the wording that I will provide.
Updates

The designs that are coming through so far are generally looking the same generic website layout. I am looking for the home page to be something different with more of a wow factor and something different to the standard page link menu accross the top of the screen. The content should be fairly minimal given that I am a new business there will be limited text for each page. I am happy to increase the budget if required as I appreciate there will be more work involved.

Reason: I am extending the deadline as the design so far are good but fairly generic and template style home pages. For the home page I am looking for something a little more striking with a visual impact.

I have increased the payment by $200 to encourage more designs. Designs need to be relevant to the business, the number of pages and content. Several designs have come through looking good but just look like a standard template with my logo added, but the content does not match the business.

The brief stated that I am looking for the home page to be something different with more of a wow factor and something different to the standard page link menu accross the top of the screen. All of the designs have come through with the navigation bar along the top and a generic layout. I have attached a couple of idea's. Obviously these do not relate to the finance and mortgage industry but you can see the sort of style that gives the site a wow factor. The other pages can be more generic, but the first page is the attention grabber. You can also see the Fonix view that I am after. These are just templates from Host Willow that I could use to build the site, I just don't have the time or creative flair. Please submit more designs. Thanks for your work to date, Rob.

Hi. Could you please submit designs based on brief and the two screen shots attached. Mobile device view should work as per screen shots. Thanks, Rob

Reason: Still looking for designs to meet the brief provided.

Industry/Entity Type

Financial

Requirements
Must have
• Colour palette to be as supplied. I will post this shortly.
Should not have
• No cheesy smiley faces
No handshaking
No money pictures
No pictures of stones
No picture of people in an office looking at things
No lime green or purple in colour
Would prefer not to have a picture of the Quayline Span or Tidewater Hall

```html
<!DOCTYPE html>
<html lang="en">
<head>
<meta charset="utf-8">
<title>Corvale Lending Group</title>
<link rel="stylesheet" href="https://fonts.googleapis.com/css2?family=Didact+Gothic&family=Roboto:wght@500&display=swap">
<style>
  :root {
    --sky: #abd0fb;
    --sky-light: #c4defd;
    --icon-blue: #1e9ad8;
    --icon-outline: #ffffff;
    --nav-text: #ffffff;
    --brand-text: #3a3d42;
    --mark-blue: #1784c4;
    --divider: #ffffff;
    --badge-fill: #ffffff;
    --badge-band: #dff0d4;
    --badge-edge: #5aa83c;
  }
  * { margin: 0; padding: 0; box-sizing: border-box; }
  html, body { width: 1200px; height: 762px; overflow: hidden; }
  body {
    background: radial-gradient(ellipse 520px 360px at 600px 440px, var(--sky-light), var(--sky));
    font-family: "Didact Gothic", sans-serif;
    position: relative;
  }

  .main-nav { position: absolute; top: 56px; left: 0; width: 1200px; height: 130px; }
  .nav-item {
    position: absolute; top: 0; width: 260px; margin-left: -130px;
    display: flex; flex-direction: column; align-items: center;
    text-decoration: none; color: var(--nav-text);
  }
  .nav-item svg { width: 90px; height: 60px; }
  .nav-label { margin-top: 12px; font-size: 39px; letter-spacing: 0.5px; line-height: 1; }
  .nav-home { left: 196px; }
  .nav-about { left: 431px; }
  .nav-services { left: 684px; }
  .nav-contact { left: 970px; }

  .brand {
    position: absolute; left: 0; top: 225px; width: 1200px; height: 450px;
  }
  .brand-mark {
    position: absolute; left: 289px; top: 115px;
    width: 200px; height: 200px; border-radius: 50%;
    background: var(--mark-blue);
  }
  .brand-divider {
    position: absolute; left: 566px; top: 0; width: 4px; height: 450px;
    background: linear-gradient(to bottom, transparent, var(--divider) 50%, transparent);
    box-shadow: 0 0 18px rgba(255,255,255,0.7);
  }
  .brand-name {
    position: absolute; left: 610px; top: 96px;
    font-family: "Roboto", sans-serif; font-weight: 500;
    font-size: 80px; line-height: 76px; color: var(--brand-text);
    letter-spacing: 1px;
  }
  .brand-name span { display: block; }

  .accreditation-badge {
    position: absolute; left: 57px; top: 688px; width: 116px; height: 42px;
    background: linear-gradient(to bottom, var(--badge-fill) 55%, var(--badge-band) 55%);
    border: 3px solid var(--badge-edge);
  }
</style>
</head>
<body>
  <nav class="main-nav">
    <a class="nav-item nav-home" href="#">
      <svg viewBox="0 0 90 60" aria-hidden="true">
        <path d="M12 52 V26 A20 16 0 0 1 32 10 H58 A20 16 0 0 1 78 26 V52 H54 V36 A9 9 0 0 0 36 36 V52 Z" fill="var(--icon-blue)" stroke="var(--icon-outline)" stroke-width="3"/>
      </svg>
      <span class="nav-label">HOME</span>
    </a>
    <a class="nav-item nav-about" href="#">
      <svg viewBox="0 0 90 60" aria-hidden="true">
        <circle cx="45" cy="15" r="10" fill="var(--icon-blue)" stroke="var(--icon-outline)" stroke-width="3"/>
        <path d="M30 54 V40 A15 14 0 0 1 60 40 V54 Z" fill="var(--icon-blue)" stroke="var(--icon-outline)" stroke-width="3"/>
      </svg>
      <span class="nav-label">ABOUT US</span>
    </a>
    <a class="nav-item nav-services" href="#">
      <svg viewBox="0 0 90 60" aria-hidden="true">
        <path d="M18 24 L45 12 L72 24 L45 36 Z" fill="var(--icon-blue)" stroke="var(--icon-outline)" stroke-width="3"/>
        <path d="M18 24 V42 L45 54 V36 Z" fill="var(--icon-blue)" stroke="var(--icon-outline)" stroke-width="3"/>
        <path d="M72 24 V42 L45 54 V36 Z" fill="var(--icon-blue)" stroke="var(--icon-outline)" stroke-width="3"/>
      </svg>
      <span class="nav-label">SERVICES</span>
    </a>
    <a class="nav-item nav-contact" href="#">
      <svg viewBox="0 0 90 60" aria-hidden="true">
        <rect x="17" y="12" width="56" height="40" rx="10" fill="var(--icon-blue)" stroke="var(--icon-outline)" stroke-width="3"/>
        <path d="M20 18 L45 36 L70 18" fill="none" stroke="var(--icon-outline)" stroke-width="3"/>
      </svg>
      <span class="nav-label">CONTACT US</span>
    </a>
  </nav>

  <section class="brand">
    <div class="brand-mark" aria-hidden="true"></div>
    <div class="brand-divider" aria-hidden="true"></div>
    <h1 class="brand-name"><span>CORVALE</span><span>LENDING</span><span>GROUP</span></h1>
  </section>

  <div class="accreditation-badge" role="img" aria-label="NLBC approved broker badge"></div>
</body>
</html>
```